Property Investment eBook Cover

I am a long established Australian property investment adviser, analyst and consultant who is now in semi-retired mode and have re-branded to reflect a more casual and personal approach to advising my property investor clients. I am writing a 'revised edition' to a book written in partnership with my father 20 years ago and need an eBook Cover for this new edition. The eBook will be uploaded to all the regular Australian providers (Tarvo Reader, Quillet Epage, Zeni, Pagemarsh)

The 3 key elements in the book cover are:

Title: The Riches Engine of Land. The word 'Property' should be larger and more prominent. eg "The Wealth Power of" could be 1/3 the size of "Property" - with both justified left

Edition: Sydney 2021. "Sydney 2021" should be the focus and dominant imagery of the eBook cover and more prominent than the Title or Author

Author: Glen Markby, The Housing Numbers Guide. The word "Author" should not appear. "The Housing Numbers Guide" should appear underneath Glen Markby and justified to Glen Markby, therefore a smaller font.

The cover should be simple, but eye-catching. No property images, more of an abstract background, than a background with an image. Our preferred colour palette is more blues/greens. Prefer SerifFonts

Copy of book published 20 years ago attached for reference only

```html
<!DOCTYPE html>
<html lang="en">
<head>
<meta charset="utf-8">
<title>The Riches Engine of Land — Sydney 2021 Edition</title>
<link rel="stylesheet" href="https://fonts.googleapis.com/css2?family=Cinzel:wght@400;500&family=Pinyon+Script&family=Montserrat:wght@500;600&display=swap">
<style>
  :root {
    --page-bg: #e9e9e9;
    --navy: #1b4f86;
    --navy-deep: #0f3e72;
    --ink: #111111;
    --paper: #ffffff;
    --gold-dark: #7d5f1a;
    --gold-mid: #b8922f;
    --gold-light: #f3d97a;
    --gold-rule: #b99423;
  }
  * { box-sizing: border-box; margin: 0; padding: 0; }
  html, body {
    width: 1200px; height: 849px; overflow: hidden;
    background: var(--page-bg);
  }
  .canvas {
    position: relative; width: 1200px; height: 849px;
    background: linear-gradient(180deg, #d8d8d8 0%, #f0f0f0 55%, #e6e6e6 100%);
  }
  .cover {
    position: absolute; left: 344px; top: 44px;
    width: 512px; height: 760px; padding: 16px;
    background:
      linear-gradient(135deg, var(--gold-dark) 0%, var(--gold-mid) 14%, var(--gold-light) 24%, var(--gold-mid) 34%, var(--gold-dark) 50%, var(--gold-mid) 64%, var(--gold-light) 78%, var(--gold-mid) 88%, var(--gold-dark) 100%);
    box-shadow: 0 14px 30px rgba(0,0,0,0.25);
  }
  .cover-inner {
    width: 100%; height: 100%;
    background: var(--paper); padding: 7px;
    display: flex; flex-direction: column;
  }
  .edition-band {
    height: 152px;
    background: linear-gradient(180deg, var(--navy) 0%, var(--navy-deep) 100%);
    color: var(--paper); text-align: center;
    display: flex; flex-direction: column; justify-content: center; align-items: center;
    gap: 6px;
  }
  .edition-label {
    font-family: "Montserrat", sans-serif; font-weight: 600;
    font-size: 13px; letter-spacing: 3px;
  }
  .edition-title {
    font-family: "Cinzel", serif; font-weight: 500;
    font-size: 56px; line-height: 1; letter-spacing: 1px;
  }
  .band-rule { height: 4px; background: var(--navy-deep); margin-top: 4px; }
  .title-block {
    flex: 1; display: flex; flex-direction: column; align-items: center; justify-content: center;
    color: var(--ink); padding: 4px 18px;
  }
  .script-row {
    width: 100%; display: flex; align-items: center; gap: 14px;
  }
  .script-row .rule {
    flex: 1; height: 3px;
    background: linear-gradient(90deg, transparent 0%, var(--gold-rule) 30%, var(--gold-rule) 100%);
  }
  .script-row .rule.right {
    background: linear-gradient(90deg, var(--gold-rule) 0%, var(--gold-rule) 70%, transparent 100%);
  }
  .script-word {
    font-family: "Pinyon Script", cursive; font-size: 54px; line-height: 1;
  }
  .title-word {
    font-family: "Cinzel", serif; font-weight: 400;
    font-size: 60px; line-height: 1.08; letter-spacing: 1px;
  }
  .title-word.lead { font-size: 84px; line-height: 1; }
  .author-band {
    height: 152px;
    background: linear-gradient(180deg, var(--navy) 0%, var(--navy-deep) 100%);
    color: var(--paper); text-align: center;
    display: flex; flex-direction: column; justify-content: center; align-items: center;
    gap: 8px;
  }
  .author-name {
    font-family: "Cinzel", serif; font-weight: 400;
    font-size: 38px; line-height: 1; letter-spacing: 1px;
  }
  .author-role {
    font-family: "Montserrat", sans-serif; font-weight: 600;
    font-size: 14px; letter-spacing: 1.5px; text-transform: uppercase;
  }
</style>
</head>
<body>
<main class="canvas">
  <article class="cover">
    <div class="cover-inner">
      <header class="edition-band">
        <p class="edition-label">EDITION:</p>
        <h2 class="edition-title">SYDNEY 2021</h2>
      </header>
      <div class="band-rule"></div>

      <section class="title-block">
        <div class="script-row">
          <span class="rule"></span><span class="script-word">The</span><span class="rule right"></span>
        </div>
        <h1>
          <span class="title-word" style="display:block;text-align:center">RICHES</span>
          <span class="title-word" style="display:block;text-align:center">ENGINE</span>
        </h1>
        <div class="script-row">
          <span class="rule"></span><span class="script-word">of</span><span class="rule right"></span>
        </div>
        <p class="title-word lead">LAND</p>
      </section>

      <div class="band-rule" style="margin-top:0;margin-bottom:4px"></div>
      <footer class="author-band">
        <p class="author-name">GLEN MARKBY</p>
        <p class="author-role">The Housing Numbers Guide</p>
      </footer>
    </div>
  </article>
</main>
</body>
</html>
```